Banner Designs for Drone Defense Ad Campaign

Corvane is a security consulting and services company that offers a service called SkyMindful. SkyMindful helps our customers identify security risks from drones and develops comprehensive protection programs. We are looking for a designer to create a banner ad in three sizes for our campaign.
Target Market(s)
Our campaign is geared to the sports and entertainment industry, specifically large event venues and their security operation.
Industry/Entity Type
Security
Font styles to use
Other font styles liked:
- Raleway
Requirements
Must have
- Banner Objective
The visual and textual content of the banner should prompt the viewer to quickly identify the service offered and the information that is available to download.
Banner Design
Logo: SkyMindful logo
Call to Action Button in Red: Get It Here (On Right or or Upper Right)
Title in Larger Font: Guide to UAS Risk Mitigation
Subtitle in smaller Font: 5 Steps to Develop Your Comprehensive UAS Defense Program
Background: Stadium with a drone flying in foreground
Font: Raleway
Banner Sizes
1 - 1200x670 pixels
2 - 1510x196 pixels
3 - 1200x628 pixels

```html
<!DOCTYPE html>
<html lang="en">
<head>
<meta charset="utf-8">
<title>SkyMindful Banner Set</title>
<link rel="stylesheet" href="https://fonts.googleapis.com/css2?family=Raleway:wght@500;600;700;900&display=swap">
<style>
  :root {
    --board: #242424;
    --white: #ffffff;
    --red: #ee1c24;
    --red-band: rgba(240, 22, 30, 0.92);
    --navy: #1f4f8f;
    --ink: #2b2b2b;
    --sky: #dcdadd;
    --trees: #5b5048;
    --water: #5f7188;
  }
  * { box-sizing: border-box; margin: 0; padding: 0; }
  html, body { width: 1200px; height: 660px; overflow: hidden; background: var(--board); }
  body { position: relative; font-family: "Raleway", sans-serif; }

  .banner { position: absolute; overflow: hidden; background: var(--white); }
  .banner--large { left: 40px; top: 70px; width: 638px; height: 356px; }
  .banner--medium { left: 713px; top: 181px; width: 436px; height: 229px; }
  .banner--leaderboard { left: 40px; top: 445px; width: 906px; height: 118px; }

  .photo {
    position: absolute; left: 0; right: 0; bottom: 0;
    background: linear-gradient(180deg,
      var(--sky) 0%, #cfc9c9 22%, #8a7d72 38%, var(--trees) 48%,
      #a49c98 58%, #c9c6c8 70%, #9aa3b1 85%, var(--water) 100%);
  }
  .banner--large .photo { top: 67px; }
  .banner--medium .photo { top: 45px; }
  .banner--leaderboard .photo {
    top: 0; right: auto; width: 303px;
    clip-path: polygon(0 0, 100% 0, 200px 100%, 0 100%);
  }

  .brand { position: absolute; color: var(--navy); text-align: right; }
  .brand__name { display: block; font-weight: 600; line-height: 1; }
  .brand__by { display: block; color: var(--ink); font-weight: 500; line-height: 1.2; }
  .banner--large .brand { left: 36px; top: 30px; }
  .banner--large .brand__name { font-size: 30px; }
  .banner--large .brand__by { font-size: 17px; }
  .banner--medium .brand { left: 33px; top: 22px; }
  .banner--medium .brand__name { font-size: 20px; }
  .banner--medium .brand__by { font-size: 11px; }
  .banner--leaderboard .brand { left: 24px; top: 84px; }
  .banner--leaderboard .brand__name { font-size: 9px; color: var(--white); }
  .banner--leaderboard .brand__by { font-size: 4.5px; color: var(--white); }

  .cta {
    position: absolute; display: flex; align-items: center; justify-content: center; gap: 8px;
    background: var(--red); color: var(--white); border-radius: 999px;
    font-weight: 600; letter-spacing: 0.06em; text-transform: uppercase;
    box-shadow: 0 0 0 12px rgba(240,240,240,0.35), 0 0 0 22px rgba(235,235,235,0.2);
  }
  .cta svg { fill: none; stroke: var(--white); stroke-width: 3.2; stroke-linecap: round; stroke-linejoin: round; }
  .banner--large .cta { left: 404px; top: 42px; width: 170px; height: 46px; font-size: 16px; }
  .banner--medium .cta { left: 287px; top: 29px; width: 112px; height: 30px; font-size: 10.5px; gap: 5px; box-shadow: 0 0 0 8px rgba(240,240,240,0.3); }
  .banner--leaderboard .cta { left: 710px; top: 37px; width: 157px; height: 42px; font-size: 16px; }

  .headline-band { position: absolute; left: 0; right: 0; background: var(--red-band); color: var(--white); text-align: center; }
  .banner--large .headline-band { top: 247px; height: 87px; padding-top: 16px; }
  .banner--medium .headline-band { top: 160px; height: 58px; padding-top: 10px; }

  .title { font-weight: 900; text-transform: uppercase; line-height: 1; letter-spacing: 0.01em; }
  .subtitle { font-weight: 600; text-transform: uppercase; line-height: 1.2; }
  .banner--large .title { font-size: 36px; }
  .banner--large .subtitle { font-size: 12.3px; margin-top: 4px; }
  .banner--medium .title { font-size: 24px; }
  .banner--medium .subtitle { font-size: 8px; margin-top: 2px; }

  .leaderboard-copy { position: absolute; left: 279px; top: 42px; width: 398px; text-align: center; color: var(--navy); }
  .leaderboard-copy .title { font-size: 24.5px; }
  .leaderboard-copy .subtitle { font-size: 8.8px; font-weight: 500; margin-top: 6px; }
</style>
</head>
<body>

  <section class="banner banner--large">
    <div class="photo" role="img" aria-label="White camera drone hovering over a lake with a blurred treeline behind"></div>
    <div class="brand"><span class="brand__name">SkyMindful</span><span class="brand__by">By Corvane</span></div>
    <a class="cta">Get It Here
      <svg width="14" height="18" viewBox="0 0 14 18"><path d="M3 2 L11 9 L3 16"/></svg></a>
    <div class="headline-band">
      <h1 class="title">Guide to UAS Risk Mitigation</h1>
      <p class="subtitle">Five steps to develop your comprehensive UAS defense program</p>
    </div>
  </section>

  <section class="banner banner--medium">
    <div class="photo" role="img" aria-label="White camera drone hovering over a lake with a blurred treeline behind"></div>
    <div class="brand"><span class="brand__name">SkyMindful</span><span class="brand__by">By Corvane</span></div>
    <a class="cta">Get It Here
      <svg width="10" height="13" viewBox="0 0 14 18"><path d="M3 2 L11 9 L3 16"/></svg></a>
    <div class="headline-band">
      <h2 class="title">Guide to UAS Risk Mitigation</h2>
      <p class="subtitle">Five steps to develop your comprehensive UAS defense program</p>
    </div>
  </section>

  <section class="banner banner--leaderboard">
    <div class="photo" role="img" aria-label="White camera drone hovering over a lake with a blurred treeline behind"></div>
    <div class="brand"><span class="brand__name">SkyMindful</span><span class="brand__by">By Corvane</span></div>
    <div class="leaderboard-copy">
      <h2 class="title">Guide to UAS Risk Mitigation</h2>
      <p class="subtitle">Five steps to develop your comprehensive UAS defense program</p>
    </div>
    <a class="cta">Get It Here
      <svg width="14" height="18" viewBox="0 0 14 18"><path d="M3 2 L11 9 L3 16"/></svg></a>
  </section>

</body>
</html>
```